Business Card Design Project

A double sided business card for presentation to business leaders in corporate.

Target Market(s)

Corporate, business professionals, HR

Industry/Entity Type

Business

Requirements
Must have
• FRONT

Logo

www.brightlanegroup.com.au

BACK

Maren Toll-Hadley
Director

+ 61 (0) 418 536 207
maren@brightlanegroup.com.au
www.brightlanegroup.com.au

Impact through energy and employee engagement

("ripples" of logo, bottom corner)

Must be:
- double sided
size: 86 x 54mm
supplied as one pdf with crop marks shown (+- 1mm, with 2-3 mm bleed)

```html
<!DOCTYPE html>
<html lang="en">
<head>
<meta charset="utf-8">
<title>Brightlane Group – Business Card</title>
<link rel="stylesheet" href="https://fonts.googleapis.com/css2?family=Questrial&display=swap">
<style>
  :root {
    --backdrop: #3a3a3a;
    --plum: #7a2a68;
    --plum-deep: #6a1f5a;
    --plum-light: #944a84;
    --blush: #ede3ea;
    --blush-mid: #dccbd7;
    --mist: #f1eff0;
    --ink: #4a4a4a;
    --white: #ffffff;
  }
  * { margin: 0; padding: 0; box-sizing: border-box; }
  html, body { width: 1200px; height: 900px; overflow: hidden; }
  body {
    position: relative;
    background: var(--backdrop);
    font-family: "Questrial", "Century Gothic", sans-serif;
  }
  .card {
    position: absolute;
    top: 245px;
    width: 571px;
    height: 358px;
    background: var(--white);
    overflow: hidden;
  }
  .card--front { left: 19px; }
  .card--back { left: 611px; }

  .front-art { position: absolute; inset: 0; width: 100%; height: 100%; }

  .wordmark {
    position: absolute;
    display: flex;
    align-items: center;
    color: var(--plum);
    font-weight: 400;
    white-space: nowrap;
  }
  .wordmark__dot {
    border-radius: 50%;
    background: var(--plum);
    flex: none;
  }
  .card--front .wordmark {
    left: 0; right: 0; top: 82px;
    justify-content: center;
    gap: 16px;
    font-size: 46px;
  }
  .card--front .wordmark__dot { width: 26px; height: 26px; }

  .front-url {
    position: absolute;
    left: 0; right: 0; bottom: 16px;
    text-align: center;
    color: var(--blush);
    font-size: 19px;
    letter-spacing: 0.5px;
  }

  .back-block { position: absolute; }
  .back-block--plum {
    left: 0; top: 0; width: 192px; height: 237px;
    background: linear-gradient(160deg, var(--plum-deep), var(--plum-light));
  }
  .back-block--blush {
    left: 0; top: 237px; width: 192px; height: 121px;
    background: var(--blush-mid);
  }
  .back-block--mist {
    left: 192px; top: 237px; width: 364px; height: 121px;
    background: var(--mist);
    border-top: 1px solid #e4dfe2;
  }
  .back-block--edge {
    left: 556px; top: 237px; width: 15px; height: 121px;
    background: var(--plum);
  }
  .card--back .wordmark {
    left: 10px; top: 270px;
    gap: 8px;
    font-size: 21px;
    line-height: 1.1;
    white-space: normal;
    width: 176px;
  }
  .card--back .wordmark__dot { width: 14px; height: 14px; }

  .person {
    position: absolute;
    right: 22px; top: 121px;
    text-align: right;
  }
  .person__name { color: var(--plum); font-size: 24px; letter-spacing: 0.3px; }
  .person__role { color: var(--ink); font-size: 17px; margin-top: 2px; }

  .contact {
    position: absolute;
    right: 24px; top: 289px;
    text-align: right;
    color: var(--ink);
    list-style: none;
    line-height: 1.2;
  }
  .contact__phone { font-size: 19px; }
  .contact__line { font-size: 16px; }
</style>
</head>
<body>
  <section class="card card--front" aria-label="Card front">
    <svg class="front-art" viewBox="0 0 571 358" preserveAspectRatio="none" aria-hidden="true">
      <defs>
        <linearGradient id="wave" x1="0" y1="0" x2="1" y2="0">
          <stop offset="0" stop-color="#6c1f5b"/>
          <stop offset="1" stop-color="#8e3f7c"/>
        </linearGradient>
      </defs>
      <path d="M380,0 C450,60 495,130 505,215 L571,200 L571,0 Z" fill="#ede3ea"/>
      <path d="M0,150 C40,200 120,238 250,240 C380,242 480,220 571,198 L571,358 L0,358 Z" fill="#9b5189"/>
      <path d="M0,185 C60,228 150,252 260,252 C380,252 470,228 571,204 L571,358 L0,358 Z" fill="url(#wave)"/>
    </svg>
    <div class="wordmark"><span class="wordmark__dot"></span><span>Brightlane Group</span></div>
    <p class="front-url">www.brightlanegroup.com.au</p>
  </section>

  <section class="card card--back" aria-label="Card back">
    <div class="back-block back-block--plum"></div>
    <div class="back-block back-block--blush"></div>
    <div class="back-block back-block--mist"></div>
    <div class="back-block back-block--edge"></div>
    <div class="wordmark"><span class="wordmark__dot"></span><span>Brightlane Group</span></div>
    <div class="person">
      <p class="person__name">Maren Toll-Hadley</p>
      <p class="person__role">Director</p>
    </div>
    <ul class="contact">
      <li class="contact__phone">+ 61 (0) 418 536 207</li>
      <li class="contact__line">maren@brightlanegroup.com.au</li>
      <li class="contact__line">www.brightlanegroup.com.au</li>
    </ul>
  </section>
</body>
</html>
```